Tech Savy small Business accountant business card design

We need a business card for a new company based in the cloud. We provide tax, business advisory, accounting, information technology solutions and back office functions to small businesses. We offer fixed fee packages with add on services as you need them. By harnessing technology we simplify small business operational processes providing valuable time and information for small business owners to grow their business. In the logo (quilbrook) we want to be able to see quil and experts. The final design should communicate achieving growth dreams and balance (ie life and $).
Updates
This project has been temporarily placed on hold until I finalize "Tech Savy small Business accountant needs a logo". I invite all designers to submit on this logo project. Once my logo is finalized I will resume this business card contest. Thanks Added Wednesday, March 19, 2014
This project has been temporarily placed on hold until I finalize "Tech Savy small Business accountant logo". I invite all designers to submit on this logo project. Once my logo is finalized I will resume this business card contest. Thanks Added Thursday, March 20, 2014
Target Market(s)
Small Business (Revenue $500,000, more than 3 employees) owners.
Industry/Entity Type
Small Business
Contact Information for Business Card
Marla Henwick (Principal)
Accountant, Tax Agent.
TEL | 0418 663 904
EMAIL | Marla.Henwick@quilbrook-mail.com.au
WEB | www.quilbrook-mail.com.au
Look and feel

```html
<!DOCTYPE html>
<html lang="en">
<head>
<meta charset="utf-8">
<title>quilbrook business card</title>
<link href="https://fonts.googleapis.com/css2?family=Open+Sans:wght@400;700&family=PT+Serif:wght@400;700&display=swap" rel="stylesheet">
<style>
  :root {
    --page: #e9e6e1;
    --paper: #f7f7f7;
    --paper-shade: #e6e6e8;
    --divider: #c9cacd;
    --blue: #1aa3d9;
    --blue-deep: #0d84c4;
    --blue-light: #3fc3ec;
    --grey-text: #8b8d91;
    --white: #ffffff;
  }
  * { margin: 0; padding: 0; box-sizing: border-box; }
  html, body { width: 1200px; height: 1062px; overflow: hidden; }
  body {
    background: var(--page);
    font-family: "Open Sans", Arial, sans-serif;
    position: relative;
  }
  .card {
    position: absolute;
    left: 170px;
    width: 860px;
    height: 480px;
    border-radius: 4px;
    overflow: hidden;
    box-shadow: 0 6px 18px rgba(0,0,0,0.18);
  }
  .card-front { top: 34px; background: linear-gradient(180deg, var(--paper) 0%, var(--paper-shade) 100%); }
  .card-back { top: 548px; background: linear-gradient(135deg, var(--blue-deep) 0%, var(--blue-light) 50%, var(--blue-deep) 100%); }

  .wordmark {
    font-family: "Open Sans", Arial, sans-serif;
    font-weight: 700;
    letter-spacing: -3px;
    line-height: 1;
    white-space: nowrap;
  }
  .tagline { font-weight: 400; line-height: 1.2; white-space: nowrap; }

  .front-brand { position: absolute; left: 60px; top: 56px; }
  .front-brand .wordmark { font-size: 112px; color: var(--blue); }
  .front-brand .tagline { font-size: 30px; color: var(--grey-text); margin-top: 30px; }
  .address {
    position: absolute; left: 60px; top: 300px;
    font-family: "PT Serif", Georgia, serif;
    font-size: 17px; color: var(--grey-text); letter-spacing: 0.5px;
  }

  .divider { position: absolute; left: 0; right: 0; top: 336px; height: 14px; background: var(--divider); }
  .band {
    position: absolute; left: 0; right: 0; top: 350px; bottom: 0;
    background: linear-gradient(180deg, var(--blue-light) 0%, var(--blue) 100%);
    color: var(--white);
  }
  .person { position: absolute; left: 60px; top: 30px; font-family: "PT Serif", Georgia, serif; }
  .person-name { font-size: 24px; font-weight: 700; }
  .person-role { font-size: 17px; margin-top: 4px; opacity: 0.9; }

  .contacts { position: absolute; left: 470px; top: 22px; list-style: none; font-size: 16px; }
  .contacts li { display: flex; align-items: center; gap: 12px; height: 28px; }
  .contacts svg { width: 16px; height: 16px; flex: none; }

  .back-brand { position: absolute; left: 60px; top: 100px; color: var(--white); }
  .back-brand .wordmark { font-size: 140px; }
  .back-brand .tagline { font-size: 34px; margin-top: 40px; }
</style>
</head>
<body>
  <section class="card card-front">
    <div class="front-brand">
      <div class="wordmark">quilbrook</div>
      <div class="tagline">Your business and accounting partner</div>
    </div>
    <div class="address">H NO:48 Harbour Lane 207 Fenwick</div>
    <div class="divider"></div>
    <div class="band">
      <div class="person">
        <div class="person-name">Marla Henwick</div>
        <div class="person-role">Accountant</div>
      </div>
      <ul class="contacts">
        <li>
          <svg viewBox="0 0 16 16" aria-hidden="true"><path d="M4 1 L6.5 1 L7.5 4.5 L5.8 5.8 Q7 9 10.2 10.2 L11.5 8.5 L15 9.5 L15 12 Q14 15 11 14.5 Q2 12 1.5 5 Q1 2 4 1 Z" fill="#fff"/></svg>
          <span>0418 663 904</span>
        </li>
        <li>
          <svg viewBox="0 0 16 16" aria-hidden="true"><g fill="none" stroke="#fff" stroke-width="1.3"><circle cx="8" cy="8" r="6.5"/><ellipse cx="8" cy="8" rx="3" ry="6.5"/><path d="M1.5 8 H14.5 M2.5 4.5 H13.5 M2.5 11.5 H13.5"/></g></svg>
          <span>www.quilbrook-mail.com.au</span>
        </li>
        <li>
          <svg viewBox="0 0 16 16" aria-hidden="true"><text x="8" y="13" text-anchor="middle" font-family="Open Sans, sans-serif" font-size="15" font-weight="700" fill="#fff">@</text></svg>
          <span>Marla.Henwick@quilbrook-mail.com.au</span>
        </li>
      </ul>
    </div>
  </section>

  <section class="card card-back">
    <div class="back-brand">
      <div class="wordmark">quilbrook</div>
      <div class="tagline">Your business and accounting partner</div>
    </div>
  </section>
</body>
</html>
```